Business Card

I need a business card that really pops for a potential customer or person who refers a personal injury lead. I want to highlight our office locations, but only address that needs to be on the card is my office's main address. I want a sleek, modern and minimalist design.

```html
<!DOCTYPE html>
<html lang="en">
<head>
<meta charset="UTF-8">
<title>Harborline Injury Lawyers – Business Card</title>
<link rel="stylesheet" href="https://fonts.googleapis.com/css2?family=Jost:wght@400&family=Nunito:wght@400;700&display=swap">
<style>
  :root {
    --backdrop: #979797;
    --card-dark: #1d1d1d;
    --card-light: #eaeaea;
    --foil: #c48d4e;
    --ink-grey: #8a8a8a;
    --ink-grey-strong: #7a7a7a;
  }
  * { margin: 0; padding: 0; box-sizing: border-box; }
  html, body {
    width: 1200px;
    height: 1200px;
    overflow: hidden;
    background: var(--backdrop);
  }
  .canvas {
    position: relative;
    width: 1200px;
    height: 1200px;
  }
  .card {
    position: absolute;
    left: 200px;
    width: 798px;
    height: 465px;
    border-radius: 36px;
  }
  .card--front {
    top: 87px;
    background: var(--card-dark);
  }
  .card--back {
    top: 612px;
    background: var(--card-light);
  }
  .brand-name {
    font-family: "Jost", sans-serif;
    font-weight: 400;
    text-transform: uppercase;
    white-space: nowrap;
  }
  .card--front .brand-name {
    position: absolute;
    left: 0;
    right: 0;
    top: 214px;
    text-align: center;
    font-size: 24px;
    letter-spacing: 0.22em;
    color: var(--foil);
  }
  .card--back .brand-name {
    position: absolute;
    left: 54px;
    top: 68px;
    font-size: 20px;
    letter-spacing: 0.2em;
    color: var(--ink-grey);
  }
  .contact {
    position: absolute;
    left: 54px;
    top: 316px;
    font-family: "Nunito", sans-serif;
    font-size: 16.5px;
    line-height: 20.5px;
    color: var(--ink-grey);
  }
  .contact p + p { margin-top: 21px; }
  .website {
    position: absolute;
    right: 59px;
    top: 398px;
    font-family: "Nunito", sans-serif;
    font-size: 16.5px;
    line-height: 20.5px;
    color: var(--ink-grey);
  }
  .website strong {
    font-weight: 700;
    color: var(--ink-grey-strong);
  }
</style>
</head>
<body>
  <main class="canvas">
    <section class="card card--front" aria-label="Card front">
      <div class="brand-name">Harborline Injury Lawyers</div>
    </section>

    <section class="card card--back" aria-label="Card back">
      <div class="brand-name">Harborline Injury Lawyers</div>
      <div class="contact">
        <p>240 Lakeview Avenue,<br>Suite 1800, Riverton, IL 60699</p>
        <p>(555) 014-2290<br>info@harborlineinjury.com</p>
      </div>
      <div class="website"><strong>harborlineinjury</strong>.com</div>
    </section>
  </main>
</body>
</html>
```